Buxley's Chowder Cafe (New Website Design)

I want an upgraded, modern, sleek, tasteful website that is easily updated internally. Our current website can be viewed at www.buxleyschowdercafe.example

Target Market(s)

Dining Customers

Industry/Entity Type

Restaurant / Hospitality

Coding

Coded - Design and coding required

Number of Pages Required

4 page

Requirements
Must have
• Modern, artful, sleek.. while maintaining a little vintage Cape Cod

```html
<!DOCTYPE html>
<html lang="en">
<head>
<meta charset="utf-8">
<title>Buxley's Restaurant &amp; Market</title>
<link rel="stylesheet" href="https://fonts.googleapis.com/css2?family=Abril+Fatface&family=Mulish:wght@400;500;600;700&display=swap">
<style>
:root{
  --header:#1f3a47;
  --page:#1f2a31;
  --footer:#1c1c1c;
  --olive:#8a7544;
  --cream:#fbf4e4;
  --white:#ffffff;
  --gold:#b39a55;
  --line:#c9c2ae;
}
*{margin:0;padding:0;box-sizing:border-box}
html,body{width:1200px;height:3157px;overflow:hidden}
body{background:var(--page);color:var(--white);font-family:'Mulish',sans-serif;position:relative}
.display{font-family:'Abril Fatface',serif;font-weight:400}
section,header,footer{position:absolute;left:0;width:1200px}
a{color:inherit;text-decoration:none}

/* header */
.site-header{top:0;height:180px;background:var(--header)}
.brand{position:absolute;left:83px;top:22px;display:flex;align-items:center;gap:8px;font-family:'Mulish',sans-serif;font-weight:700;font-size:17px;letter-spacing:1px;color:var(--white)}
.brand-dot{width:14px;height:14px;border-radius:50%;border:2px solid var(--white)}
.sign-in{position:absolute;right:84px;top:48px;font-size:13px;font-weight:700;letter-spacing:.3px}
.main-nav{position:absolute;left:83px;right:84px;top:136px;display:flex;justify-content:space-between;font-size:13px;font-weight:700;letter-spacing:.2px}
.main-nav .caret::after{content:"";display:inline-block;width:5px;height:5px;border-right:1.5px solid #fff;border-bottom:1.5px solid #fff;transform:rotate(45deg);margin-left:10px;position:relative;top:-3px}

/* hero */
.hero{top:180px;height:584px;background:radial-gradient(ellipse at 50% 50%,#5c5c50 0%,#3f4540 55%,#2d3431 100%)}
.hero-title{position:absolute;top:178px;width:100%;text-align:center;font-size:80px;color:var(--cream);letter-spacing:1px}
.hero-sub{position:absolute;top:305px;width:100%;text-align:center;font-size:27px;font-weight:600;letter-spacing:3px;color:var(--cream)}
.hero-actions{position:absolute;top:365px;left:0;width:100%;display:flex;justify-content:center;align-items:center;gap:20px}
.btn-solid{background:var(--header);border-bottom:2px solid var(--line);padding:12px 27px;font-size:16px}
.btn-link{text-decoration:underline;font-size:16px;text-underline-offset:3px}

/* welcome */
.welcome{top:764px;height:518px;background:linear-gradient(90deg,var(--olive) 0%,var(--olive) 55%,#7d6a3f 75%,#6f5e38 100%)}
.welcome-photo{position:absolute;right:0;top:0;width:540px;height:518px;background:radial-gradient(ellipse at 45% 50%,#a89472 0%,#8c7a52 45%,rgba(138,117,68,0) 75%)}
.welcome h2{position:absolute;left:83px;top:128px;font-size:42px}
.welcome p{position:absolute;left:83px;width:430px;font-size:16px;line-height:21px}
.welcome .p1{top:206px}
.welcome .p2{top:331px}

/* special */
.special{top:1282px;height:565px}
.special-photo{position:absolute;left:0;top:26px;width:520px;height:539px;background:radial-gradient(ellipse at 40% 55%,#b7565a 0%,#c9a27a 40%,#b8742e 75%,#8a4a1c 100%)}
.special-info{position:absolute;left:603px;top:0}
.eyebrow{position:absolute;top:152px;font-size:13px;letter-spacing:1.3px;white-space:nowrap;display:flex;align-items:center;gap:12px}
.eyebrow::after{content:"";width:165px;height:1px;background:var(--line)}
.special h2{position:absolute;top:200px;font-size:42px;white-space:nowrap}
.special .note{position:absolute;top:257px;font-size:16px;white-space:nowrap}
.special .price{position:absolute;top:304px;font-size:26px}
.special .served{position:absolute;top:347px;font-size:16px;white-space:nowrap}
.btn-outline{position:absolute;top:401px;padding:10px 7px;border-top:1px solid var(--line);border-bottom:1px solid var(--line);font-size:16px;white-space:nowrap}

/* menus */
.menus{top:1847px;height:544px}
.menus h2{position:absolute;top:87px;width:100%;text-align:center;font-size:42px}
.menus .center-btn{position:absolute;top:164px;left:533px;width:134px;text-align:center;padding:11px 0;border-top:1px solid var(--line);border-bottom:1px solid var(--line);font-size:16px}
.carousel{position:absolute;top:239px;left:0;height:292px;width:1200px}
.menu-card{position:absolute;top:0;width:333px;height:292px}
.card-1{left:0;background:radial-gradient(circle at 40% 45%,#c08a3e 0%,#e0a21c 45%,#f2f2ee 80%)}
.card-2{left:347px;background:radial-gradient(circle at 60% 60%,#e0305e 0%,#c4224a 45%,#2b2b2b 90%)}
.card-3{left:693px;background:radial-gradient(circle at 50% 50%,#9cbf5a 0%,#e7ead8 50%,#f4f1ea 85%)}
.card-4{left:1040px;width:160px;background:radial-gradient(circle at 40% 60%,#b04a3a 0%,#6b6f78 55%,#3a3d44 100%)}
.car-arrow{position:absolute;top:126px;width:40px;height:40px;background:rgba(60,60,50,.75);display:flex;align-items:center;justify-content:center}
.car-prev{left:83px}
.car-next{left:1076px}

/* merchandise */
.merch{top:2391px;height:377px;background:linear-gradient(180deg,#4a5658 0%,#5a6462 50%,#4b5556 100%)}
.merch h2{position:absolute;top:122px;width:100%;text-align:center;font-size:42px}
.merch .center-btn{position:absolute;top:204px;left:520px;width:160px;text-align:center;padding:11px 0;border-top:1px solid var(--line);border-bottom:1px solid var(--line);font-size:16px}

/* footer */
.site-footer{top:2782px;height:375px;background:var(--footer)}
.map{position:absolute;left:0;top:0;width:331px;height:375px;background:linear-gradient(135deg,#dfe1e3 0%,#e8e9ea 50%,#d6dcd2 100%)}
.loc-label{position:absolute;left:415px;top:57px;font-size:18px}
.loc-item{position:absolute;left:415px;display:flex;gap:14px;font-size:16px;line-height:21px}
.loc-item svg{flex:none;margin-top:2px}
.loc-addr{top:112px}
.loc-hours{top:188px}
.loc-phone{top:274px}
.accent{color:var(--gold)}
.footer-brand{position:absolute;right:84px;top:58px;display:flex;align-items:center;gap:8px;font-weight:700;font-size:18px;letter-spacing:1px}
.takeout{position:absolute;right:84px;top:218px;text-align:right;font-size:16px;line-height:21px}
.follow{position:absolute;right:84px;top:294px;display:flex;align-items:center;gap:16px;font-size:16px;font-weight:700}
.social-dot{width:22px;height:22px;border-radius:50%;background:var(--white)}
</style>
</head>
<body>

<header class="site-header">
  <a class="brand" href="#"><span class="brand-dot"></span>BUXLEY'S</a>
  <a class="sign-in" href="#">SIGN IN</a>
  <nav class="main-nav">
    <a href="#">ORDER ONLINE</a>
    <a class="caret" href="#">MENUS</a>
    <a class="caret" href="#">SEAFOOD MARKETPLACE</a>
    <a href="#">GIFT CARDS</a>
    <a href="#">MERCHANDISE</a>
    <a class="caret" href="#">ABOUT US</a>
    <a href="#">BECOME A VIP</a>
  </nav>
</header>

<section class="hero" role="img" aria-label="Close-up of a creamy seafood pasta with scallions">
  <h1 class="hero-title display">BUXLEY'S</h1>
  <p class="hero-sub">RESTAURANT &amp; MARKET</p>
  <div class="hero-actions">
    <a class="btn-solid" href="#">Our Menu</a>
    <a class="btn-link" href="#">Become A VIP</a>
  </div>
</section>

<section class="welcome">
  <div class="welcome-photo" role="img" aria-label="Baked stuffed oyster with lemon on a white plate"></div>
  <h2 class="display">Welcome to Buxley's</h2>
  <p class="p1">Established in 1938, Buxley's Restaurant offers classic Cape Cod fare featuring fresh seafood and creative comfort cuisine. Our comfortable atmosphere includes a lively pub, two fireplace dining rooms, and a Seafood Market with takeout.</p>
  <p class="p2">Located in the charming seaside village of Harwick Point, Buxley's strives to please each guest with the best dining experience possible.</p>
</section>

<section class="special">
  <div class="special-photo" role="img" aria-label="Plate of slow roasted prime rib with green beans and a baked potato"></div>
  <div class="special-info">
    <div class="eyebrow">DAILY SPECIAL</div>
    <h2 class="display">Slow Roasted Prime Rib</h2>
    <p class="note">(While it lasts) Avaiable after 4:00 PM</p>
    <p class="price display">$30</p>
    <p class="served">Served with choice of Starch &amp; Vegetable</p>
    <a class="btn-outline" href="#">More Daily Specials</a>
  </div>
</section>

<section class="menus">
  <h2 class="display">Various Menus</h2>
  <a class="center-btn" href="#">View All Menus</a>
  <div class="carousel">
    <div class="menu-card card-1" role="img" aria-label="Bowl of soup topped with a toasted crouton and cheese"></div>
    <div class="menu-card card-2" role="img" aria-label="Pink cocktail with a sugared rim and lime"></div>
    <div class="menu-card card-3" role="img" aria-label="Green salad with cucumber, onion and cranberries"></div>
    <div class="menu-card card-4" role="img" aria-label="Berry cocktail garnished with blueberries"></div>
    <a class="car-arrow car-prev" href="#" aria-label="Previous"><svg width="14" height="20" viewBox="0 0 14 20"><path d="M11 2 3 10l8 8" fill="none" stroke="#fff" stroke-width="2.5"/></svg></a>
    <a class="car-arrow car-next" href="#" aria-label="Next"><svg width="14" height="20" viewBox="0 0 14 20"><path d="m3 2 8 8-8 8" fill="none" stroke="#fff" stroke-width="2.5"/></svg></a>
  </div>
</section>

<section class="merch" role="img" aria-label="Shelves of folded branded t-shirts in the shop">
  <h2 class="display">Get Our Merchandise!</h2>
  <a class="center-btn" href="#">Go To Merchandise</a>
</section>

<footer class="site-footer">
  <div class="map" role="img" aria-label="Street map showing the restaurant location"></div>
  <h3 class="loc-label display">Location</h3>
  <div class="loc-item loc-addr">
    <svg width="14" height="18" viewBox="0 0 14 18"><path d="M7 0a7 7 0 0 0-7 7c0 5 7 11 7 11s7-6 7-11a7 7 0 0 0-7-7zm0 9.5A2.5 2.5 0 1 1 7 4.5a2.5 2.5 0 0 1 0 5z" fill="#fff"/></svg>
    <div>Harwick Point<br>118 Harbor Ln<br>Harwick Point, MA 02999</div>
  </div>
  <div class="loc-item loc-hours">
    <svg width="16" height="16" viewBox="0 0 16 16"><circle cx="8" cy="8" r="7" fill="none" stroke="#fff" stroke-width="1.6"/><path d="M8 4v4.5l3 1.5" fill="none" stroke="#fff" stroke-width="1.6"/></svg>
    <div>Monday - Tuesday:<br>Closed<br>Wednesday - Sunday:<br>11:30 am - 9:00 pm</div>
  </div>
  <div class="loc-item loc-phone">
    <svg width="16" height="16" viewBox="0 0 24 24"><path d="M6.6 10.8a15 15 0 0 0 6.6 6.6l2.2-2.2a1 1 0 0 1 1-.25 11.4 11.4 0 0 0 3.6.57 1 1 0 0 1 1 1V20a1 1 0 0 1-1 1A17 17 0 0 1 3 4a1 1 0 0 1 1-1h3.5a1 1 0 0 1 1 1c0 1.25.2 2.45.57 3.57a1 1 0 0 1-.25 1z" fill="#fff"/></svg>
    <div>(555) 014-2280<br><span class="accent">Reservations by Phone Only</span></div>
  </div>
  <div class="footer-brand"><span class="brand-dot"></span>BUXLEY'S</div>
  <p class="takeout">For takeout and seafood market call:<br><span class="accent">555-014-7731</span></p>
  <div class="follow">Follow: <span class="social-dot" aria-label="Social page"></span></div>
</footer>

</body>
</html>
```